Redesign website for small print company

Vindaborgprent is a small printing company in Iceland mainly servicing Students, schools, etc. We are also doing all kind of other jobs, like business cards, book printing, brochure printing etc. We are also selling books online.
Our website is: www.vindaborgprent.is
What we are looking for is:
- Web Design (Uncoded - PSD layout only)
- Mobile friendly design, using our current color scheme: Red, green, yellow and light gray.
- Clean simple design
- Simple, light and easy to use.
- More menu Items/drop down
Industry/Entity Type
Digital Printing
Number of Pages Required
5+ page
Requirements
Must have
- Easy navigation
- Designed for mobile
- Current color scheme (see logo)
Nice to have
- Icon based products

```html
<!DOCTYPE html>
<html lang="en">
<head>
<meta charset="utf-8">
<title>Vindaborgprent – Popular Navigation Menu</title>
<link href="https://fonts.googleapis.com/css2?family=Poppins:wght@400;500;600&family=Tinos&display=swap" rel="stylesheet">
<style>
  :root {
    --red: #ef3b33;
    --green: #1f6b3d;
    --sale-green: #3cc46a;
    --yellow: #ffd400;
    --ink: #2a2a2a;
    --muted: #8a8a8a;
    --line: #ececec;
    --dot: #e6e6e6;
    --bg: #ffffff;
  }
  * { box-sizing: border-box; margin: 0; padding: 0; }
  html, body { width: 1200px; height: 1200px; overflow: hidden; background: var(--bg); }
  body { position: relative; font-family: "Poppins", sans-serif; color: var(--ink); }

  .backdrop { position: absolute; inset: 0; }

  .site {
    position: absolute; left: 0; top: 316px; width: 1200px; height: 674px;
    background: #fff;
    box-shadow: 0 20px 40px rgba(0,0,0,0.08);
  }

  .topbar {
    position: absolute; left: 0; top: 0; width: 100%; height: 50px;
    border-bottom: 1px solid #f2f2f2;
    font-size: 13px; color: #444;
  }
  .topbar .contact { position: absolute; left: 86px; top: 9px; display: flex; gap: 18px; align-items: center; }
  .topbar .contact span, .topbar .hours { display: flex; align-items: center; gap: 6px; }
  .topbar .hours { position: absolute; right: 88px; top: 9px; }

  .brand {
    position: absolute; left: 522px; top: 36px;
    display: flex; align-items: center; gap: 8px;
    font-weight: 600; font-size: 21px; color: var(--ink); letter-spacing: 0.2px;
  }
  .brand .mark { width: 24px; height: 24px; background: var(--red); }

  .language {
    position: absolute; left: 86px; top: 76px;
    display: flex; align-items: center; gap: 8px;
    font-size: 13px; color: var(--muted);
  }

  .tools { position: absolute; right: 82px; top: 76px; display: flex; gap: 10px; }
  .tool {
    position: relative; width: 34px; height: 24px; border: 1px solid #e4e4e4; border-radius: 12px;
    display: flex; align-items: center; justify-content: center;
  }
  .tool.avatar { width: 24px; border-radius: 50%; background: #eee; border: none; }
  .tool .badge {
    position: absolute; top: -8px; right: 0; background: #2f80ed; color: #fff;
    font-size: 7px; border-radius: 6px; padding: 0 3px; line-height: 10px;
  }

  .divider { position: absolute; left: 19px; right: 19px; top: 125px; height: 1px; background: var(--line); }

  .mainnav {
    position: absolute; left: 0; top: 136px; width: 100%; height: 34px;
    font-size: 13px; font-weight: 500; color: #333;
  }
  .mainnav .item { position: absolute; top: 5px; display: flex; align-items: center; gap: 6px; }
  .mainnav .item.active::after {
    content: ""; position: absolute; left: -1px; right: -1px; top: 27px; height: 2px; background: var(--red);
  }
  .gift {
    position: absolute; left: 933px; top: 4px; width: 93px; height: 20px; border-radius: 10px;
    background: var(--yellow); color: #fff; font-size: 13px; text-align: center; line-height: 20px;
  }
  .store { position: absolute; left: 1038px; top: 5px; color: var(--muted); }

  .menu-panel { position: absolute; left: 0; top: 170px; width: 280px; height: 504px; }
  .categories { list-style: none; position: absolute; left: 88px; top: 88px; }
  .categories li { font-size: 19px; color: #555; height: 39px; position: relative; }
  .categories li.sale { color: var(--sale-green); }
  .categories .new {
    position: absolute; left: 64px; top: -6px; font-size: 9px; font-weight: 600; color: var(--red);
  }
  .see-all {
    position: absolute; left: 47px; top: 405px; width: 186px; height: 53px; border-radius: 27px;
    background: var(--red); color: #fff; font-weight: 600; font-size: 14px; letter-spacing: 0.5px;
    display: flex; align-items: center; justify-content: center;
    box-shadow: 0 10px 20px rgba(239,59,51,0.3);
  }

  .tile { position: absolute; top: 170px; height: 504px; }
  .tile.leaflet { left: 280px; width: 304px; background: linear-gradient(160deg, #e9e9ee 0%, #8d8fc4 40%, #3f6b86 75%, #d9d0c4 100%); }
  .tile.books { left: 587px; width: 303px; background: linear-gradient(120deg, #e8397f 0%, #c9c5bb 35%, #3d3f44 60%, #f2d21e 100%); }
  .tile.cards { left: 894px; width: 306px; background: linear-gradient(90deg, #9e9e9e 0%, #f3f3f3 15%, #ffffff 60%, #e2e2e2 100%); }
  .tile-label {
    position: absolute; left: 0; bottom: 0; width: 100%; height: 44px; background: var(--green);
    color: #fff; font-size: 18px; font-weight: 500; padding: 0 14px;
    display: flex; align-items: center; justify-content: space-between;
  }

  .caption {
    position: absolute; left: 187px; top: 1020px;
    font-family: "Tinos", serif; font-size: 9.5px; line-height: 13px; color: #9a9a9a;
  }
</style>
</head>
<body>
  <svg class="backdrop" width="1200" height="1200" viewBox="0 0 1200 1200" aria-hidden="true">
    <g fill="#eeeeee">
      <circle cx="56" cy="13" r="9"/><circle cx="84" cy="13" r="9"/><circle cx="111" cy="13" r="9"/><circle cx="138" cy="13" r="9"/><circle cx="165" cy="13" r="9"/><circle cx="192" cy="13" r="9"/>
      <circle cx="56" cy="46" r="9"/><circle cx="84" cy="46" r="9"/><circle cx="111" cy="46" r="9"/><circle cx="138" cy="46" r="9"/><circle cx="165" cy="46" r="9"/><circle cx="192" cy="46" r="9"/>
    </g>
    <defs>
      <pattern id="dotgrid" x="436" y="96" width="48" height="80" patternUnits="userSpaceOnUse">
        <circle cx="2" cy="2" r="2" fill="#e4e4e4"/>
      </pattern>
      <pattern id="dotgrid-low" x="436" y="1056" width="48" height="80" patternUnits="userSpaceOnUse">
        <circle cx="2" cy="2" r="2" fill="#e4e4e4"/>
      </pattern>
    </defs>
    <rect x="436" y="96" width="680" height="170" fill="url(#dotgrid)"/>
    <rect x="436" y="1056" width="680" height="90" fill="url(#dotgrid-low)"/>
    <path d="M58 316 A220 220 0 0 1 494 316" fill="none" stroke="#e8e8e8" stroke-width="1"/>
    <g fill="none" stroke="#555" stroke-width="0.8">
      <path d="M776 1013 C830 1012 870 1002 890 990"/>
      <path d="M776 1039 C850 1039 900 1020 934 990"/>
      <path d="M1048 990 C1080 1010 1140 1012 1200 1013"/>
      <path d="M1096 990 C1130 1020 1170 1038 1200 1040"/>
    </g>
  </svg>

  <main class="site">
    <div class="topbar">
      <div class="contact">
        <span>
          <svg width="11" height="11" viewBox="0 0 24 24" fill="#555"><path d="M6.6 10.8a15 15 0 0 0 6.6 6.6l2.2-2.2a1 1 0 0 1 1-.25 11.4 11.4 0 0 0 3.6.57 1 1 0 0 1 1 1V20a1 1 0 0 1-1 1A17 17 0 0 1 3 4a1 1 0 0 1 1-1h3.5a1 1 0 0 1 1 1c0 1.25.2 2.45.57 3.6a1 1 0 0 1-.25 1z"/></svg>
          555 0142
        </span>
        <span>
          <svg width="11" height="9" viewBox="0 0 24 18" fill="#555"><path d="M0 0h24v18H0z M2 2l10 7 10-7" stroke="#fff" stroke-width="2"/></svg>
          verk@vindaborgprent.is
        </span>
      </div>
      <div class="hours">
        <svg width="11" height="11" viewBox="0 0 24 24" fill="none" stroke="#555" stroke-width="2"><circle cx="12" cy="12" r="10"/><path d="M12 6v6l4 2"/></svg>
        Mon – Fri: 9-17
      </div>
    </div>

    <div class="brand"><span class="mark"></span>VINDABORGPRENT</div>

    <div class="language">
      <svg width="15" height="15" viewBox="0 0 20 20"><circle cx="10" cy="10" r="9" fill="#3b5bb5"/><path d="M1 10h18M10 1v18" stroke="#fff" stroke-width="4"/><path d="M1 10h18M10 1v18" stroke="#e23b3b" stroke-width="2"/></svg>
      English - UK
      <svg width="8" height="6" viewBox="0 0 10 6" fill="none" stroke="#999" stroke-width="1.5"><path d="M1 1l4 4 4-4"/></svg>
    </div>

    <div class="tools">
      <div class="tool"><svg width="11" height="11" viewBox="0 0 24 24" fill="none" stroke="#333" stroke-width="2.5"><circle cx="10" cy="10" r="7"/><path d="M15 15l6 6"/></svg></div>
      <div class="tool"><span class="badge">47</span><svg width="11" height="11" viewBox="0 0 24 24" fill="none" stroke="#333" stroke-width="2"><path d="M2 3h3l3 12h12l2-8H7"/><circle cx="9" cy="20" r="1.5"/><circle cx="18" cy="20" r="1.5"/></svg></div>
      <div class="tool avatar"></div>
    </div>

    <div class="divider"></div>

    <nav class="mainnav">
      <span class="item" style="left:105px">Home</span>
      <span class="item active" style="left:190px">Popular
        <svg width="8" height="6" viewBox="0 0 10 6" fill="none" stroke="#333" stroke-width="1.6"><path d="M1 5l4-4 4 4"/></svg></span>
      <span class="item" style="left:296px">Shop
        <svg width="8" height="6" viewBox="0 0 10 6" fill="none" stroke="#333" stroke-width="1.6"><path d="M1 1l4 4 4-4"/></svg></span>
      <span class="item" style="left:378px">Job Submit</span>
      <span class="item" style="left:487px">About Us</span>
      <span class="gift">Gift Cards</span>
      <span class="store">Find a store</span>
    </nav>

    <section class="menu-panel">
      <ul class="categories">
        <li>Invitation</li>
        <li>Flyers</li>
        <li>Menus<span class="new">NEW</span></li>
        <li class="sale">Sale</li>
      </ul>
      <div class="see-all">SEE ALL</div>
    </section>

    <div class="tile leaflet" role="img" aria-label="Photo of folded leaflets and printed brochures">
      <div class="tile-label">A3 Folded leaflet
        <svg width="28" height="20" viewBox="0 0 28 20" fill="none" stroke="#fff" stroke-width="2.4"><path d="M2 10h22M16 2l8 8-8 8"/></svg>
      </div>
    </div>
    <div class="tile books" role="img" aria-label="Photo of printed book covers"></div>
    <div class="tile cards" role="img" aria-label="Photo of a printed business card stack"></div>
  </main>

  <div class="caption">VINDABORGPRENT<br>POPULAR<br>NAVIGATION MENU</div>
</body>
</html>
```